FloraNova Microbiome Graphics

We are a team of researchers looking for a landing page design with graphics. We are FloraNova and our logo is up on www.floranova-labs.example. We like the look and feel of our logo, and want corresponding graphics.

We want white background with blue/green color scheme of the logo.

Our Mission:

We recognize that every person hosts a unique community of microorganisms. Not only is your microbiome unique, it also has a unique response to lifestyle modification including diet and supplementation which could have a massive impact on your health and wellness. Our mission is to provide targeted supplementation, personalized nutrition plans, and sleep and circadian rhythm analysis techniques to improve your Ill unique microbiome and maximize your individual health. Our goal is to translate your unique gut bacteria into a personalized plan for you to maximize your well being.
Updates

Project Deadline Extended Reason: We don't like these designs currently, and we want more time to get better designs. We thought we would be provided with much more designs but most of these are amateurish and don't follow the prompt. Added Friday, July 21, 2017

Target Market(s)

Investors, Patients, Scientists

Industry/Entity Type

Health And Wellness

Font styles to use
Other font styles liked:
• See logo on floranova-labs.example

Colors
0492cd
33a6d7
85cae6
9bcb3c
acd036
cadf82
ffffff

Requirements
Must have
• -landing page with our mission and a picture of the gut micobiome. This would have a texture of an abstract gut microbiome. Please see the attached samples. Want something more custom.
• -A custom graphic for the gut micobiome. This would have a texture of an abstract gut microbiome. Please see the attached samples. Want something more custom. This would be related to our mission.
• -some custom graphics that showcase gut bacteria. Please see the ideas on microbiome.jpg attachments. We want to emphasize positive gut bacteria as we are trying to improve the gut health.
• -An abstract of the gut bacteria with a human body but make the human body abstract.
Nice to have
• Clean sophisticated graphics. Communicates feeling of improving health by improving gut health.
• We would probably prefer something on the lines of a healthy living "rainforest" or living "city " or "farm" or "horizon " or " universe " ring represented from within. perhaps side by side images to demonstrate the equilibrium between good and bad , the force ( moon quest fans ) , or the gut bacteria

```html
<!DOCTYPE html>
<html lang="en">
<head>
<meta charset="utf-8">
<title>FloraNova — Good Bacteria for Good Health</title>
<link href="https://fonts.googleapis.com/css2?family=Source+Sans+3:wght@400;600;700&family=Oswald:wght@700&family=Great+Vibes&display=swap" rel="stylesheet">
<style>
  :root{
    --blue:#0492cd;
    --blue-mid:#33a6d7;
    --blue-light:#85cae6;
    --green:#9bcb3c;
    --green-lime:#acd036;
    --green-pale:#cadf82;
    --white:#ffffff;
    --ink:#111111;
    --dark:#262626;
    --gut:#c9563d;
  }
  *{margin:0;padding:0;box-sizing:border-box}
  html,body{width:844px;height:1200px;overflow:hidden;background:var(--white)}
  body{position:relative;font-family:"Source Sans 3",sans-serif;color:var(--ink)}

  .brand{position:absolute;left:0;top:0;width:311px;height:103px;background:var(--dark);
    clip-path:polygon(0 0,100% 0,100% 72%,88% 100%,0 100%);display:flex;align-items:center;gap:12px;padding-left:24px;z-index:3}
  .brand-dot{width:26px;height:26px;border-radius:50%;background:var(--green)}
  .brand-name{color:var(--white);font-size:33px;font-weight:400;letter-spacing:.5px}

  .nav{position:absolute;left:311px;top:0;width:533px;height:84px;z-index:2}
  .nav-row{height:42px;display:flex;align-items:center;font-weight:600;font-size:16px;letter-spacing:-.3px;color:#1e2a10}
  .nav-top{background:var(--green-pale);padding-left:23px;gap:30px}
  .nav-bottom{background:var(--green);justify-content:space-between;padding:0 22px 0 23px;border-bottom:2px solid var(--blue)}
  .search{margin-left:auto;margin-right:13px;width:154px;height:27px;border-radius:8px;background:#eef3e6;
    color:#8a8a8a;font-weight:400;font-size:16px;text-align:right;padding:3px 10px 0 0}

  .hero{position:absolute;left:0;top:84px;width:844px;height:389px;
    background:linear-gradient(180deg,var(--blue) 0%,var(--blue-mid) 55%,#0b4a6a 80%,#000 100%)}
  .hero-figure{position:absolute;left:90px;top:0;width:450px;height:389px;
    background:radial-gradient(ellipse 120px 150px at 50% 45%,var(--gut) 0%,rgba(201,86,61,.6) 55%,rgba(133,202,230,.35) 80%,rgba(133,202,230,0) 100%)}
  .headline{position:absolute;right:26px;top:52px;width:300px;text-align:center;color:var(--white);line-height:1}
  .headline .l1{font-size:44px;font-weight:400}
  .headline .l1 b{font-family:"Oswald",sans-serif;font-weight:700;color:#000;font-size:50px}
  .headline .l2{font-size:42px;font-weight:600;margin-top:10px}
  .headline .l3{font-size:44px;font-weight:400;margin-top:8px}
  .headline .l3 span{font-family:"Great Vibes",cursive;color:var(--green-lime);font-size:66px}

  .bacteria{position:absolute;top:377px;width:240px;text-align:center}
  .bacteria .disc{width:168px;height:168px;margin:0 auto;border-radius:50%;border:6px solid var(--green-pale)}
  .bacteria h3{font-size:28px;font-weight:600;margin-top:10px;letter-spacing:-.3px}
  .b-ecoli{left:67px}.b-ecoli .disc{background:radial-gradient(circle,#f04a2e 0%,#fbd6cc 65%,#fff 100%)}
  .b-bifido{left:308px}.b-bifido .disc{background:radial-gradient(circle,#2fc14a 0%,#c9f0c4 65%,#fff 100%)}
  .b-lacto{left:539px}.b-lacto .disc{background:radial-gradient(circle,#1a8ee8 0%,#8fd1f5 60%,#fff 100%)}

  .mission-title{position:absolute;top:662px;width:844px;text-align:center;font-size:44px;font-weight:700;letter-spacing:-.5px}
  .cards{position:absolute;top:744px;left:27px;width:801px;height:197px}
  .card{position:absolute;top:0;width:187px;height:197px;border:1px solid #555;border-top:10px solid var(--green);text-align:center}
  .card svg{position:absolute;left:50%;transform:translateX(-50%)}
  .card p{position:absolute;left:0;right:0;font-size:14.5px;font-weight:600;line-height:1.2;letter-spacing:-.3px}
  .c1{left:0}.c2{left:202px}.c3{left:405px}.c4{left:616px;width:185px}
  .runner{position:absolute;left:50%;top:34px;width:70px;height:80px;transform:translateX(-50%);
    background:radial-gradient(ellipse at center,var(--blue) 30%,rgba(4,146,205,0) 70%)}

  .statement{position:absolute;top:980px;width:844px;text-align:center;font-size:15px;line-height:1.3}

  .footer{position:absolute;top:1115px;left:0;width:844px;height:69px;background:var(--green);
    display:flex;align-items:center;padding:10px 14px 0 18px;font-size:14px}
  .footer nav{margin-left:auto;display:flex;gap:22px}
  .footer-base{position:absolute;top:1184px;left:0;width:844px;height:16px;background:var(--dark)}
</style>
</head>
<body>
  <header>
    <div class="brand"><span class="brand-dot"></span><span class="brand-name">FloraNova</span></div>
    <div class="nav">
      <div class="nav-row nav-top"><span>Meet the Microbiome</span><span>Microbiome Testing</span><span class="search">Search</span></div>
      <div class="nav-row nav-bottom"><span>Products</span><span>About us</span><span>The Company</span><span>Contact us</span></div>
    </div>
  </header>

  <section class="hero">
    <div class="hero-figure" role="img" aria-label="Abstract human torso with the digestive tract and gut microbiome"></div>
    <h1 class="headline">
      <div class="l1">Good <b>Bacteria</b></div>
      <div class="l2">for</div>
      <div class="l3">Good <span>Health</span></div>
    </h1>
  </section>

  <div class="bacteria b-ecoli"><div class="disc" role="img" aria-label="Red Escherichia coli cells"></div><h3>Escherichia Coli</h3></div>
  <div class="bacteria b-bifido"><div class="disc" role="img" aria-label="Green Bifidobacteria cells"></div><h3>Bifidobacteria</h3></div>
  <div class="bacteria b-lacto"><div class="disc" role="img" aria-label="Blue Lactobacilli cells"></div><h3>Lactobacilli</h3></div>

  <h2 class="mission-title">Our Mission</h2>

  <div class="cards">
    <div class="card c1">
      <svg width="60" height="80" viewBox="0 0 60 80" style="top:28px">
        <rect x="10" y="0" width="40" height="12" rx="3" fill="none" stroke="var(--blue)" stroke-width="5"/>
        <rect x="2" y="14" width="56" height="64" rx="12" fill="var(--blue)"/>
        <rect x="14" y="38" width="32" height="14" fill="#fff"/>
      </svg>
      <p style="top:135px">provide targeted<br>supplementation</p>
    </div>
    <div class="card c2">
      <svg width="104" height="74" viewBox="0 0 104 74" style="top:26px">
        <rect x="0" y="0" width="10" height="74" fill="var(--blue)"/>
        <rect x="94" y="16" width="10" height="58" fill="var(--blue)"/>
        <rect x="0" y="44" width="104" height="10" fill="var(--blue)"/>
        <circle cx="24" cy="24" r="10" fill="var(--blue)"/>
        <rect x="40" y="16" width="50" height="24" rx="5" fill="var(--blue)"/>
      </svg>
      <p style="top:138px">sleep and circadian rhythm<br>analysis techniques</p>
    </div>
    <div class="card c3">
      <svg width="130" height="88" viewBox="0 0 130 88" style="top:26px">
        <rect width="130" height="88" fill="var(--blue)"/>
        <g fill="#fff" font-family="Source Sans 3,sans-serif" font-size="11" font-weight="700">
          <rect x="8" y="6" width="8" height="14"/>
          <g fill="none" stroke="#fff" stroke-width="1"><rect x="20" y="6" width="12" height="14"/><rect x="34" y="6" width="12" height="14"/><rect x="48" y="6" width="12" height="14"/><rect x="62" y="6" width="12" height="14"/><rect x="76" y="6" width="12" height="14"/><rect x="90" y="6" width="12" height="14"/><rect x="104" y="6" width="12" height="14"/></g>
          <text x="22" y="17" fill="#fff">S</text><text x="36" y="17" fill="#fff">M</text><text x="50" y="17" fill="#fff">W</text><text x="64" y="17" fill="#fff">T</text><text x="78" y="17" fill="#fff">F</text><text x="92" y="17" fill="#fff">S</text>
          <rect x="8" y="26" width="8" height="14"/><rect x="8" y="46" width="8" height="14"/><rect x="8" y="66" width="8" height="14"/>
        </g>
      </svg>
      <p style="top:138px">personalized nutrition<br>plans</p>
    </div>
    <div class="card c4">
      <div class="runner" role="img" aria-label="Running athlete silhouette"></div>
      <p style="top:132px">maximize your<br>individual health</p>
    </div>
  </div>

  <p class="statement">We recognize that every person hosts a unique community of microorganisms. Not only is your microbiome unique,<br>it also has a unique response to lifestyle modification including diet and<br>supplementation which could have a massive impact on your health and wellness</p>

  <footer class="footer">
    <span>© 2017 FloraNova All Rights Reserved.</span>
    <nav><span>Privacy Policy</span><span>Disclaimer</span><span>Sitemap</span></nav>
  </footer>
  <div class="footer-base"></div>
</body>
</html>
```